Construction company stationary design

We're wanting to develop a new professional stationary set for a newly establised property related business using our existing logo (attached). Business incorporates renovations, property investment and property development.

Specifically needing letter head, business cards, envelopes, email signature and need to get tshirt and caps embroydered.

Looking for something quite modern but professional using white, black and green.

Investment

```html
<!DOCTYPE html>
<html lang="en">
<head>
<meta charset="utf-8">
<title>Email Signature – Norvale Constructions</title>
<link rel="stylesheet" href="https://fonts.googleapis.com/css2?family=Source+Sans+3:wght@400;600;700&family=PT+Sans+Narrow:wght@400;700&display=swap">
<style>
  :root {
    --ink: #1a1a1a;
    --paper: #ffffff;
  }
  html, body {
    margin: 0;
    padding: 0;
    width: 1200px;
    height: 494px;
    overflow: hidden;
    background: var(--paper);
  }
  .signature {
    position: relative;
    width: 1200px;
    height: 494px;
    color: var(--ink);
    font-family: "Source Sans 3", Arial, sans-serif;
  }
  .contact {
    position: absolute;
    left: 79px;
    top: 76px;
    font-size: 21px;
    line-height: 26.5px;
    letter-spacing: -0.2px;
  }
  .contact p { margin: 0; }
  .contact .role,
  .contact .office { font-weight: 600; }
  .contact .office .detail { font-weight: 400; }
  .contact .web { margin-top: 19px; }
  .contact .web .label { font-weight: 600; }
  .disclaimer {
    position: absolute;
    left: 79px;
    top: 332px;
    width: 1090px;
    font-family: "PT Sans Narrow", "Arial Narrow", sans-serif;
    font-size: 14px;
    line-height: 21.5px;
  }
  .disclaimer h2 {
    margin: 0;
    font-size: 14px;
    font-weight: 700;
  }
  .disclaimer p { margin: 0; }
</style>
</head>
<body>
<div class="signature">
  <div class="contact">
    <p class="closing">Regards,</p>
    <p class="name">Sam Ridley</p>
    <p class="role">General Manager | Norvale Constructions</p>
    <p class="office">Dubai Office : <span class="detail">P.O. Box: 40218 | Dubai | UAE</span>&nbsp; Tel: <span class="detail">+971 4 5550182</span> | Fax: <span class="detail">+971 4 5550182</span></p>
    <p class="po-box">P.O. Box: 40219</p>
    <p class="web"><span class="label">Web :</span> &nbsp;www.norvaleconstructions.com</p>
  </div>
  <div class="disclaimer">
    <h2>DISCLAIMER</h2>
    <p>This email and any files transmitted with it are confidential and intended solely for the use of the individual or entity to which they are addressed. If you are not the intended recipient, you should not copy it, re-transmit it, use it or disclose its contents, you should notify the sender of receiving the email in error, and immediately delete the copy from your system. Please note that any views or opinions presented in this email are solely those of the author and do not necessarily represent those of BrightwaveTechnologies. Finally, the recipient should check this email and any attachments for the presence of viruses . BrightwaveTechnologies accepts no liability for any damage caused by any virus transmitted by this email.</p>
  </div>
</div>
</body>
</html>
```